Stationery - Jewellers
Business Card, Letterhead, Envelope.
I need double sided standard sized Business Card [3.5" x 2"]
Anything that looks good. Including the fonts in logo.
Professional
Imran Kazemi
Proprietor
148 Wexcombe Lane
BX4 7QT
Leeds
United Kingdom
info@corwinthegoldcrafts.co.uk
corwinthegoldcrafts.co.uk
I will welcome any ideas.
Logo and tagline: Professionals in making your loved ones smile..
Website address.
Find us on Facebook/Twitter logos.

```html
<!DOCTYPE html>
<html lang="en">
<head>
<meta charset="utf-8">
<title>Corwin Stationery Set</title>
<link rel="stylesheet" href="https://fonts.googleapis.com/css2?family=Cormorant+Garamond:wght@600&family=Open+Sans:wght@400;600&display=swap">
<style>
  :root{
    --bg:#e9e6e1;
    --paper:#ffffff;
    --ink:#2b2b2b;
    --muted:#6f6f6f;
    --black:#141414;
    --gold-dark:#a8781c;
    --gold:#d4a53c;
    --gold-light:#f4dc8e;
    --silver:#c9c9c9;
    --gold-grad:linear-gradient(135deg,var(--gold-dark),var(--gold-light) 50%,var(--gold) 80%,var(--gold-dark));
  }
  *{box-sizing:border-box;margin:0;padding:0}
  html,body{width:1200px;height:509px;overflow:hidden;background:var(--bg)}
  body{position:relative;font-family:"Open Sans",sans-serif;color:var(--ink)}
  .piece{position:absolute;background:var(--paper);box-shadow:0 2px 6px rgba(0,0,0,.25);overflow:hidden}
  .brand{display:flex;align-items:center;gap:5px}
  .brand-name{font-family:"Cormorant Garamond",serif;font-weight:600;color:var(--gold-dark);line-height:1}
  .brand-dot{border-radius:50%;background:var(--black);border:2px solid var(--gold)}
  .details{font-size:4.6px;line-height:1.5;color:var(--muted);white-space:nowrap}
  .details b{color:var(--ink);font-weight:600}
  .corner{position:absolute}

  /* business card front */
  .card-front{left:19px;top:67px;width:207px;height:120px}
  .card-front .corner{left:0;top:0;width:207px;height:120px}
  .card-front .brand{position:absolute;left:14px;top:22px}
  .card-front .brand-name{font-size:24px}
  .card-front .brand-dot{width:22px;height:22px}
  .card-front .person{position:absolute;left:14px;top:76px;font-size:5.5px;font-weight:600;text-transform:uppercase;letter-spacing:.5px}
  .card-front .person span{display:block;font-weight:400;color:var(--muted);font-size:4.5px;text-transform:none;letter-spacing:0}
  .card-front .details{position:absolute;left:100px;top:68px}

  /* business card black */
  .card-dark{left:235px;top:67px;width:211px;height:120px;background:var(--black)}
  .card-dark .brand{position:absolute;left:16px;top:14px}
  .card-dark .brand-name{font-size:24px;color:var(--gold)}
  .card-dark .brand-dot{width:24px;height:24px}
  .card-dark .gold-bar{position:absolute;left:0;bottom:9px;width:120px;height:3px;background:var(--gold-grad)}
  .card-dark .person{position:absolute;left:16px;top:80px;font-size:5.5px;font-weight:600;color:#fff;text-transform:uppercase;letter-spacing:.5px}
  .card-dark .person span{display:block;font-weight:400;color:var(--silver);font-size:4.5px;text-transform:none;letter-spacing:0}
  .card-dark .details{position:absolute;left:108px;top:50px;color:var(--silver)}
  .card-dark .details b{color:var(--gold)}

  /* business card back */
  .card-back{left:139px;top:197px;width:221px;height:120px}
  .card-back .brand{position:absolute;left:96px;top:22px}
  .card-back .brand-dot{width:30px;height:30px}
  .card-back .tagline{position:absolute;left:14px;top:70px;font-size:6px;color:var(--gold-dark);font-style:italic}
  .card-back .site{position:absolute;left:14px;bottom:12px;font-size:4.5px;color:var(--muted)}
  .card-back .social{position:absolute;right:14px;bottom:10px;display:flex;gap:3px}
  .card-back .social i{display:block;width:8px;height:8px;background:#3a5a98}
  .card-back .social i+i{background:#33a9dd}

  /* letterhead */
  .letterhead{left:456px;top:24px;width:175px;height:432px}
  .letterhead .corner{left:0;top:0;width:175px;height:432px}
  .letterhead .brand{position:absolute;left:12px;top:16px}
  .letterhead .brand-name{font-size:19px}
  .letterhead .brand-dot{width:16px;height:16px}
  .letterhead .details{position:absolute;left:106px;top:12px;font-size:3.8px}
  .letterhead .watermark{position:absolute;left:42px;top:150px;width:90px;height:90px;border-radius:50%;background:#f1f1f1;border:2px solid #e4e4e4}

  /* envelopes */
  .env-back{left:650px;top:40px;width:512px;height:190px}
  .env-back .flap{position:absolute;left:0;top:0}
  .env-back .seal{position:absolute;left:236px;top:8px;width:40px;height:40px;border-radius:50%;background:#f2f2f2;border:2px solid var(--silver)}

  .env-mid{left:690px;top:140px;width:472px;height:210px}
  .env-mid .brand{position:absolute;right:28px;top:40px}
  .env-mid .brand-dot{width:30px;height:30px}

  .env-front{left:700px;top:300px;width:440px;height:172px}
  .env-front .flap{position:absolute;left:0;top:0}
  .env-front .brand{position:absolute;left:196px;top:6px}
  .env-front .brand-dot{width:36px;height:36px}
  .env-front .details{position:absolute;left:16px;top:96px;font-size:4.6px}
  .env-front .stamp{position:absolute;right:20px;bottom:14px;width:40px;height:40px;border-radius:50%;background:#eeeeee}
</style>
</head>
<body>

<section class="piece card-front" aria-label="Business card front">
  <svg class="corner" viewBox="0 0 207 120" width="207" height="120" aria-hidden="true">
    <defs><linearGradient id="gf" x1="0" y1="0" x2="1" y2="1"><stop offset="0" stop-color="#a8781c"/><stop offset=".5" stop-color="#f4dc8e"/><stop offset="1" stop-color="#c4912c"/></linearGradient></defs>
    <path d="M0 0H60Q20 8 0 40Z" fill="url(#gf)"/>
    <path d="M207 120H150Q190 110 207 82Z" fill="url(#gf)"/>
  </svg>
  <div class="brand"><span class="brand-name">Corwin</span><span class="brand-dot"></span></div>
  <p class="person">Imran Kazemi<span>Proprietor</span></p>
  <p class="details">148 Wexcombe Lane, BX4 7QT<br>Leeds, United Kingdom<br><b>Phone:</b> 0113 496 0718<br><b>Mobile:</b> 07700 900 412<br><b>Email:</b> info@corwinthegoldcrafts.co.uk<br><b>Web:</b> corwinthegoldcrafts.co.uk</p>
</section>

<section class="piece card-dark" aria-label="Business card dark version">
  <div class="brand"><span class="brand-name">Corwin</span><span class="brand-dot"></span></div>
  <p class="details">148 Wexcombe Lane, BX4 7QT<br>Leeds, United Kingdom<br><b>Phone:</b> 0113 496 0718<br><b>Mobile:</b> 07700 900 412<br><b>Email:</b> info@corwinthegoldcrafts.co.uk<br><b>Web:</b> corwinthegoldcrafts.co.uk</p>
  <p class="person">Imran Kazemi<span>Proprietor</span></p>
  <div class="gold-bar"></div>
</section>

<section class="piece card-back" aria-label="Business card back">
  <div class="brand"><span class="brand-dot"></span></div>
  <p class="tagline">Professionals in making your loved ones smile..</p>
  <p class="site">corwinthegoldcrafts.co.uk</p>
  <div class="social" aria-label="Social links"><i></i><i></i></div>
</section>

<section class="piece letterhead" aria-label="Letterhead">
  <svg class="corner" viewBox="0 0 175 432" width="175" height="432" aria-hidden="true">
    <defs><linearGradient id="gl" x1="0" y1="0" x2="1" y2="1"><stop offset="0" stop-color="#a8781c"/><stop offset=".5" stop-color="#f4dc8e"/><stop offset="1" stop-color="#c4912c"/></linearGradient></defs>
    <path d="M0 0H40Q14 10 0 36Z" fill="url(#gl)"/>
    <path d="M175 432H130Q160 424 175 396Z" fill="url(#gl)"/>
  </svg>
  <div class="brand"><span class="brand-name">Corwin</span><span class="brand-dot"></span></div>
  <p class="details">148 Wexcombe Lane, BX4 7QT<br>Leeds, United Kingdom<br><b>Phone:</b> 0113 496 0718<br><b>Email:</b> info@corwinthegoldcrafts.co.uk<br><b>Web:</b> corwinthegoldcrafts.co.uk</p>
  <div class="watermark" aria-hidden="true"></div>
</section>

<section class="piece env-back" aria-label="Envelope back">
  <svg class="flap" viewBox="0 0 512 190" width="512" height="190" aria-hidden="true">
    <defs><linearGradient id="gs" x1="0" y1="0" x2="0" y2="1"><stop offset="0" stop-color="#9a9a9a"/><stop offset=".7" stop-color="#dcdcdc"/><stop offset="1" stop-color="#b5b5b5"/></linearGradient></defs>
    <path d="M0 0H512V20Q256 110 0 20Z" fill="url(#gs)"/>
  </svg>
  <div class="seal"></div>
</section>

<section class="piece env-mid" aria-label="Envelope front">
  <div class="brand"><span class="brand-dot"></span></div>
</section>

<section class="piece env-front" aria-label="Envelope with gold flap">
  <svg class="flap" viewBox="0 0 440 172" width="440" height="172" aria-hidden="true">
    <defs><linearGradient id="ge" x1="0" y1="0" x2="1" y2="0"><stop offset="0" stop-color="#a8781c"/><stop offset=".5" stop-color="#f4dc8e"/><stop offset="1" stop-color="#c4912c"/></linearGradient></defs>
    <path d="M0 0H440V30Q220 80 0 30Z" fill="url(#ge)"/>
  </svg>
  <div class="brand"><span class="brand-dot"></span></div>
  <p class="details">148 Wexcombe Lane, BX4 7QT<br>Leeds, United Kingdom<br><b>Phone:</b> 0113 496 0718<br><b>Email:</b> info@corwinthegoldcrafts.co.uk<br><b>Web:</b> corwinthegoldcrafts.co.uk</p>
  <div class="stamp" aria-hidden="true"></div>
</section>

</body>
</html>
```